Brisk Lumo Entertainment

I need a web design for my Business for better online promotions and services.. The name of my company is Brisk Lumo its a entertainment company music, events, networking and so on.. What I do is help artist create and finish projects such as mix tapes, music videos, and book performances in order to create a platform and i also offer representation to help grow there brands or business... I also work with and help develop independent artists!!!

Target Market(s)

Hip hop and R&B industry

Industry/Entity Type

Entertainment Industry

Number of Pages Required

1 page

Requirements
Must have
• Must display My previous and upcoming work i want people to see the quality I provide in my service.. I have more videos that I want to upload on there to show more work.... I would like to bring all the separate promotions and campaigns that I previously had and currently have all one platform for everybody to see and to find more easily instead having everything so spread out..
Nice to have
• Creativity thats going to compliment my work and quality..

```html
<!DOCTYPE html>
<html lang="en">
<head>
<meta charset="utf-8">
<title>Brisk Lumo Entertainment</title>
<link rel="stylesheet" href="https://fonts.googleapis.com/css2?family=Cinzel:wght@400;700&family=Hind:wght@400;500;600&family=Oswald:wght@400;500&display=swap">
<style>
:root{
  --red:#e3252f;
  --red-dark:#7d1a20;
  --bg:#1f1e26;
  --bg-deep:#17161c;
  --text:#d9d9de;
  --muted:#8e8d96;
  --white:#ffffff;
}
*{margin:0;padding:0;box-sizing:border-box}
html,body{width:1200px;height:2936px;overflow:hidden;background:var(--bg);font-family:"Hind",sans-serif;color:var(--text)}
.page{position:relative;width:1200px;height:2936px;overflow:hidden}
.abs{position:absolute}

/* hero */
.hero{left:0;top:0;width:1200px;height:675px;background:linear-gradient(100deg,#8a1a22 0%,#3a1b22 35%,#221f26 60%,#2a2a2e 100%)}
.hero-photo{left:0;top:0;width:1200px;height:675px;background:radial-gradient(ellipse at 78% 30%,rgba(90,90,90,.35),transparent 55%),linear-gradient(180deg,rgba(0,0,0,.15),rgba(20,18,24,.55))}
.menu-icon{left:172px;top:21px;width:20px}
.menu-icon span{display:block;height:2px;background:var(--white);margin-bottom:3px}
.nav-signup{left:888px;top:18px;font-size:12px;letter-spacing:.5px;color:var(--white)}
.nav-signin{left:960px;top:13px;width:66px;height:25px;border:1.5px solid var(--red);color:var(--red);font-size:11px;text-align:center;line-height:24px;letter-spacing:.5px}
.brand{left:0;width:1200px;text-align:center;font-family:"Cinzel",serif;color:var(--red);font-weight:400}
.hero-brand{top:292px;font-size:48px;letter-spacing:2px}
.hero-mark{left:576px;top:218px;width:48px;height:48px;border:2px solid var(--red);border-radius:50%}
.tagline{left:0;top:376px;width:1200px;text-align:center;font-size:16px;color:var(--white)}
.btn{top:426px;height:44px;font-size:12px;font-weight:600;text-align:center;line-height:44px;letter-spacing:.5px}
.btn-outline{left:458px;width:134px;border:1.5px solid var(--red);color:var(--red)}
.btn-solid{left:607px;width:134px;background:var(--red);color:var(--white)}
.scroll-mouse{left:592px;top:620px;width:14px;height:22px;border:1.5px solid var(--red);border-radius:7px}

/* video sections */
.section-title{font-family:"Cinzel",serif;color:var(--red);font-size:33px;letter-spacing:1px}
.section-text{font-size:13px;line-height:21px;color:var(--muted)}
.explore{font-size:11px;color:var(--red);display:flex;align-items:center;gap:8px}
.explore i{display:block;width:34px;height:1px;background:var(--red);position:relative}
.explore i::after{content:"";position:absolute;right:0;top:-3px;width:6px;height:6px;border-top:1px solid var(--red);border-right:1px solid var(--red);transform:rotate(45deg)}
.card{width:329px;height:298px;border:3px solid var(--white)}
.card-photo{position:absolute;inset:0}
.card-caption{position:absolute;left:0;right:0;bottom:0;height:48px;background:linear-gradient(transparent,rgba(0,0,0,.75));font-family:"Oswald",sans-serif;color:var(--white);font-size:18px;line-height:48px;padding-left:22px}
.card-red .card-photo{background:linear-gradient(160deg,#a2323a,#6e1c22)}
.card-grey .card-photo{background:linear-gradient(160deg,#6a6a6a,#1e1e1e)}
.badge{position:absolute;top:-36px;left:50%;margin-left:-23px;width:46px;height:58px;background:var(--red);color:var(--white);text-align:center;font-family:"Oswald",sans-serif;line-height:1}
.badge .b1{font-size:9px;display:block;margin-top:6px}
.badge .b2{font-size:20px;display:block;margin-top:2px}
.badge .b3{font-size:8px;display:block;margin-top:2px}
.chev{position:absolute;top:110px;width:30px;height:70px}

/* about */
.about-pattern{left:0;top:1620px;width:1200px;height:485px;background:linear-gradient(180deg,transparent 0%,rgba(120,20,28,.25) 55%,rgba(120,20,28,.35) 100%)}
.about-title{left:0;top:1622px;width:1200px;text-align:center}
.about-text{left:280px;top:1690px;width:640px;text-align:center}
.about-explore{left:543px;top:1804px}
.insta-strip{left:62px;top:1878px;width:695px;height:138px;display:flex}
.insta-strip div{flex:1;height:100%}
.insta-icon{left:808px;top:1910px;width:42px;height:42px;background:var(--red);border-radius:6px}
.insta-label{left:790px;top:1970px;width:80px;text-align:center;font-size:11px;color:var(--muted)}

/* watch videos */
.watch{left:0;top:2105px;width:1200px;height:450px;background:radial-gradient(ellipse at 50% 55%,#1f3a1c 0%,#0f1a0f 40%,#0b0b0d 80%)}
.play{left:545px;top:2260px;width:110px;height:110px;border-radius:50%;background:rgba(60,60,60,.7)}
.play::before{content:"";position:absolute;left:15px;top:15px;width:80px;height:80px;border-radius:50%;background:var(--red)}
.play::after{content:"";position:absolute;left:50px;top:42px;border-left:22px solid var(--white);border-top:13px solid transparent;border-bottom:13px solid transparent}
.watch-label{left:0;top:2383px;width:1200px;text-align:center;font-size:16px;color:var(--white)}
.thumbs{left:0;top:2555px;width:1200px;height:85px;background:var(--bg-deep);display:flex;gap:3px;padding:0 10px}
.thumb{position:relative;flex:1;background:linear-gradient(160deg,#5a5a5a,#1c1c1c)}
.thumb.active{background:linear-gradient(160deg,#2e5a2a,#101810);border-top:3px solid var(--red)}
.thumb span{position:absolute;right:6px;bottom:4px;font-size:10px;color:var(--white)}
.thumb-arrow{left:592px;top:2546px;border-left:8px solid transparent;border-right:8px solid transparent;border-bottom:9px solid var(--red)}

/* footer */
.foot-brand{top:2702px;font-size:22px;letter-spacing:2px}
.foot-mark{left:586px;top:2670px;width:28px;height:28px;border:2px solid var(--red);border-radius:50%}
.foot-line{left:0;width:1200px;text-align:center;font-size:12px;color:var(--muted)}
.socials{left:508px;top:2848px;display:flex;gap:26px}
.socials span{width:14px;height:14px;border-radius:50%;background:var(--muted)}
</style>
</head>
<body>
<div class="page">

  <header class="abs hero">
    <div class="abs hero-photo" role="img" aria-label="Dark moody photo of an artist in a hat against trees, red tinted"></div>
    <div class="abs menu-icon"><span></span><span></span><span></span></div>
    <div class="abs nav-signup">SIGN UP</div>
    <div class="abs nav-signin">SIGN IN</div>
    <div class="abs hero-mark"></div>
    <div class="abs brand hero-brand">BRISK LUMO</div>
    <p class="abs tagline">Brisk Lumo its a entertainment company music, events, networking and so on...</p>
    <div class="abs btn btn-outline">PROMO VIDEO</div>
    <div class="abs btn btn-solid">OUR SERVICES</div>
    <div class="abs scroll-mouse"></div>
  </header>

  <section class="upcoming">
    <h2 class="abs section-title" style="left:172px;top:755px">UPCOMING VIDEOS</h2>
    <p class="abs section-text" style="left:172px;top:817px;width:345px">I must explain to you how all this mistaken idea of denouncing pleasure and praising pain was born and I will give you a complete account of the system, and expound the actual teachings of the great explorer of the truth, the master-builder of human happiness. No one rejects, dislikes, or avoids pleasure itself, because it is pleasure, but because those who do not know how to are extremely painful.</p>
    <div class="abs explore" style="left:172px;top:1010px">Expore More <i></i></div>

    <article class="abs card card-grey" style="left:612px;top:765px">
      <div class="card-photo" role="img" aria-label="Black and white photo of two men posing at a party"></div>
      <div class="card-caption">THE STANDARD LOREM IPSUM SINCE</div>
      <div class="badge"><span class="b1">ADDED</span><span class="b2">08</span><span class="b3">JAN 2017</span></div>
    </article>
    <article class="abs card card-red" style="left:964px;top:765px">
      <div class="card-photo" role="img" aria-label="Red tinted photo of a performer dancing"></div>
      <svg class="chev" style="left:100px" viewBox="0 0 30 70"><polyline points="4,2 26,35 4,68" fill="none" stroke="#fff" stroke-width="2"/></svg>
      <div class="card-caption">THE STANDARD LOREM IPSUM SINCE</div>
      <div class="badge"><span class="b1">ADDED</span><span class="b2">08</span><span class="b3">JAN 2017</span></div>
    </article>
  </section>

  <section class="recent">
    <article class="abs card card-red" style="left:-94px;top:1155px">
      <div class="card-photo" role="img" aria-label="Red tinted photo of a rapper on stage"></div>
      <svg class="chev" style="left:196px" viewBox="0 0 30 70"><polyline points="26,2 4,35 26,68" fill="none" stroke="#fff" stroke-width="2"/></svg>
      <div class="card-caption">THE STANDARD LOREM IPSUM SINCE</div>
      <div class="badge"><span class="b1">ADDED</span><span class="b2">08</span><span class="b3">JAN 2017</span></div>
    </article>
    <article class="abs card card-grey" style="left:258px;top:1155px">
      <div class="card-photo" role="img" aria-label="Black and white photo of two men seated together"></div>
      <div class="card-caption">THE STANDARD LOREM IPSUM SINCE</div>
      <div class="badge"><span class="b1">ADDED</span><span class="b2">08</span><span class="b3">JAN 2017</span></div>
    </article>
    <h2 class="abs section-title" style="left:684px;top:1145px">RECENT VIDEOS</h2>
    <p class="abs section-text" style="left:684px;top:1207px;width:345px">I must explain to you how all this mistaken idea of denouncing pleasure and praising pain was born and I will give you a complete account of the system, and expound the actual teachings of the great explorer of the truth, the master-builder of human happiness. No one rejects, dislikes, or avoids pleasure itself, because it is pleasure, but because those who do not know how to are extremely painful.</p>
    <div class="abs explore" style="left:684px;top:1400px">Expore More <i></i></div>
  </section>

  <section class="about">
    <div class="abs about-pattern" role="img" aria-label="Faint red equalizer bar pattern in the background"></div>
    <h2 class="abs section-title about-title">ABOUT BRISK LUMO</h2>
    <p class="abs section-text about-text">I must explain to you how all this mistaken idea of denouncing pleasure and praising pain was born and I will give you a complete account of the system, and expound the actual teachings of the great explorer of the truth, the master-builder of human happiness. No one rejects, dislikes, or avoids pleasure itself, because it is pleasure, but because those who do not know how to are extremely painful.</p>
    <div class="abs explore about-explore">Expore More <i></i></div>
    <div class="abs insta-strip">
      <div role="img" aria-label="Performer in pink suit on stage" style="background:linear-gradient(160deg,#b0306a,#3a1420)"></div>
      <div role="img" aria-label="Group photo at an event" style="background:linear-gradient(160deg,#6a4a2a,#1c140e)"></div>
      <div role="img" aria-label="Artist in patterned jacket seated" style="background:linear-gradient(160deg,#3a5a8a,#1a1e2a)"></div>
      <div role="img" aria-label="Performer in a dim venue" style="background:linear-gradient(160deg,#5a3a2a,#140e0c)"></div>
      <div role="img" aria-label="Rapper performing under red lights" style="background:linear-gradient(160deg,#8a2a3a,#18080c)"></div>
    </div>
    <div class="abs insta-icon"></div>
    <div class="abs insta-label">INSTAFEED</div>
  </section>

  <section class="videos">
    <div class="abs watch" role="img" aria-label="Dark green lit photo of an artist with raised hands"></div>
    <div class="abs play"></div>
    <div class="abs watch-label">Watch Videos</div>
    <div class="abs thumbs">
      <div class="thumb" role="img" aria-label="Video still"><span>02:40</span></div>
      <div class="thumb" role="img" aria-label="Video still"><span>03:20</span></div>
      <div class="thumb" role="img" aria-label="Video still"><span>01:40</span></div>
      <div class="thumb" role="img" aria-label="Video still"><span>04:20</span></div>
      <div class="thumb active" role="img" aria-label="Current video still"><span>02:20</span></div>
      <div class="thumb" role="img" aria-label="Video still"><span>02:40</span></div>
      <div class="thumb" role="img" aria-label="Video still"><span>02:40</span></div>
      <div class="thumb" role="img" aria-label="Video still"><span>04:20</span></div>
      <div class="thumb" role="img" aria-label="Video still"><span>02:40</span></div>
    </div>
    <div class="abs thumb-arrow"></div>
  </section>

  <footer>
    <div class="abs foot-mark"></div>
    <div class="abs brand foot-brand">BRISK LUMO</div>
    <p class="abs foot-line" style="top:2766px">228, lorem ipsum. street area. dosist -858545</p>
    <p class="abs foot-line" style="top:2794px">Telephone : 1800 555 012 &nbsp;|&nbsp; Email : info@brisklumo.com</p>
    <div class="abs socials"><span></span><span></span><span></span><span></span><span></span></div>
    <p class="abs foot-line" style="top:2886px;font-size:11px">©2017 Brisk Lumo. &nbsp;|&nbsp; Privacy &nbsp;|&nbsp; Terms of Use</p>
  </footer>

</div>
</body>
</html>
```